Letterhead

We are looking for a basic letterhead. It should include our logo, website - northpeakkitchenware.com, phone 907.418.3952, toll free 855.392.6180, and fax 907.418.5263, along with our address 4837 Birchwood Lane, Anchorage, AK 99517. I want something that will look good printed in color or black and white.

```html
<!DOCTYPE html>
<html lang="en">
<head>
<meta charset="utf-8">
<title>North Peak Kitchenware — Letterhead</title>
<link rel="stylesheet" href="https://fonts.googleapis.com/css2?family=Source+Sans+3:wght@400;700&display=swap">
<style>
  :root {
    --paper: #ffffff;
    --brand-blue: #1f4e8c;
    --brand-red: #c43d4b;
    --ink: #3a3a3a;
  }
  html, body {
    margin: 0;
    padding: 0;
    overflow: hidden;
  }
  body {
    width: 971px;
    height: 1200px;
    background: var(--paper);
    font-family: "Source Sans 3", Arial, sans-serif;
  }
  .letterhead {
    position: relative;
    width: 971px;
    height: 1200px;
    background: var(--paper);
  }
  .brand-name {
    position: absolute;
    top: 118px;
    left: 0;
    width: 100%;
    margin: 0;
    text-align: center;
    font-size: 40px;
    font-weight: 700;
    letter-spacing: 1px;
    color: var(--brand-blue);
  }
  .footer-band {
    position: absolute;
    left: 0;
    bottom: 0;
    width: 100%;
    height: 22px;
    background: var(--brand-red);
  }
  .address {
    position: absolute;
    left: 240px;
    top: 1106px;
    margin: 0;
    font-style: normal;
    font-size: 14px;
    line-height: 20px;
    text-align: right;
    color: var(--ink);
    width: 190px;
  }
  .contact-list {
    position: absolute;
    left: 515px;
    top: 1066px;
    margin: 0;
    display: grid;
    grid-template-columns: 64px 12px auto;
    row-gap: 0;
    font-size: 15px;
    line-height: 20px;
  }
  .contact-list dt {
    color: var(--brand-red);
  }
  .contact-list .sep {
    color: var(--brand-red);
  }
  .contact-list dd {
    margin: 0;
    color: var(--ink);
  }
</style>
</head>
<body>
  <main class="letterhead">
    <h1 class="brand-name">NORTH PEAK KITCHENWARE</h1>

    <address class="address">
      4837 Birchwood Lane,<br>
      Anchorage, AK 99517
    </address>

    <dl class="contact-list">
      <dt>Mobile</dt><span class="sep">:</span><dd>907.418.3952</dd>
      <dt>Fax</dt><span class="sep">:</span><dd>907.418.5263</dd>
      <dt>Toll free</dt><span class="sep">:</span><dd>855.392.6180</dd>
      <dt>Email</dt><span class="sep">:</span><dd>orders@northpeakkitchenware.com</dd>
      <dt>Website</dt><span class="sep">:</span><dd>northpeakkitchenware.com</dd>
    </dl>

    <div class="footer-band"></div>
  </main>
</body>
</html>
```